Kitchen and cabinet shop needs new website

Benvoe Cabinets is a mid-sized, family run cabinet shop that is in the process of updating it's image after being handed over to the second generation. It's been in the business for almost 30 years and our designers have lots of experience in the design, home building and renovation industry. Our business offers free home consultations or a customer can visit our showroom to start the design process. Whether the client is a designer, home builder or homeowner we can help create the kitchen and space you're after by helping every step of the way.

The website needs to showcase our past work, (pictures to be included), show the different styles (eg. traditional, modern) and different areas of the home we can produce cabinets for. We created a new logo with Sketch hive that needs to be included in the website as well as the colours. I would like 5 pages;
-Home page
-About us
-portfolio/gallery
-services
-contact us

I would like the website to have a contemporary look, nothing too busy or complicated.

I will attach some pictures with the different styles of our work I mentioned above and provide content for each job.
Updates

Target Market(s)

home owners, designer, home builders, business owners

Industry/Entity Type

Home Builder

Number of Pages Required

5+ page

Font styles to use
Sans Serif

Requirements
Must have
• home page, about us page, gallery/portfolio page-showing various pictures of our work and different styles, services page and contact us.
• Use logo and similar colours as in logo for the scheme
• more content and pictures to follow...

```html
<!DOCTYPE html>
<html lang="en">
<head>
<meta charset="utf-8">
<title>Benvoe Cabinets – Custom woodwork and cabinetry</title>
<link rel="stylesheet" href="https://fonts.googleapis.com/css2?family=Montserrat:wght@400;500;600&family=Roboto:wght@400;500&display=swap">
<style>
:root{
  --blue:#2a5caa;
  --blue-dark:#1f4f9c;
  --orange:#e8601c;
  --ink:#333;
  --muted:#666;
  --footer:#121212;
  --footer-base:#0a0a0a;
  --footer-text:#8a8a8a;
  --white:#fff;
}
*{margin:0;padding:0;box-sizing:border-box}
html,body{width:691px;height:1200px;overflow:hidden;background:var(--white)}
body{position:relative;font-family:"Roboto",sans-serif;color:var(--ink)}
.abs{position:absolute}

/* top bar */
.topbar{left:0;top:0;width:691px;height:24px;background:var(--blue);color:var(--white);font-size:7px;}
.topbar .phone{left:62px;top:8px;letter-spacing:.2px}
.topbar svg{right:62px;top:8px}

/* header */
.header{left:0;top:24px;width:691px;height:62px;background:var(--white);border-bottom:1px solid #e4e4e4}
.brand{left:64px;top:17px;display:flex;align-items:center;gap:6px}
.brand .mark{width:18px;height:18px;background:var(--blue)}
.brand .name{font-family:"Montserrat",sans-serif;font-weight:600;font-size:15px;color:var(--blue);letter-spacing:.5px}
.nav{right:64px;top:27px;display:flex;font-family:"Montserrat",sans-serif;font-size:7px;}
.nav a{color:#222;text-decoration:none;padding:0 12px;border-left:1px solid #ddd;line-height:14px}
.nav a:first-child{border-left:none;color:var(--orange)}
.nav a:last-child{padding-right:0}

/* hero */
.hero{left:0;top:86px;width:691px;height:328px;background:linear-gradient(120deg,#d9d8d4 0%,#b9b7b2 45%,#6d6a66 75%,#3a3735 100%)}
.hero-caption{left:120px;top:180px;width:450px;height:74px;background:rgba(40,40,40,.55);text-align:center;color:var(--white)}
.hero-caption h1{font-family:"Montserrat",sans-serif;font-weight:500;font-size:15px;margin-top:13px;letter-spacing:.2px}
.hero-caption p{font-size:7px;line-height:15px;margin:6px 18px 0}
.dots{display:flex;gap:5px}
.dot{width:6px;height:6px;border-radius:50%;background:#ccc}
.dot.on{background:var(--blue)}
.hero .dots{left:330px;top:310px}

/* intro */
.section-title{font-family:"Montserrat",sans-serif;font-weight:500;font-size:12px;color:var(--blue);text-align:center;width:691px;left:0}
.intro-text{left:64px;width:563px;top:462px;font-size:6.4px;line-height:15px;text-align:center;color:#333}
.sub{left:0;width:691px;text-align:center;font-size:6.4px;top:521px}

/* service cards */
.card{top:539px;width:130px;height:161px;background:var(--blue);box-shadow:0 6px 8px rgba(0,0,0,.3)}
.card.active{background:var(--orange)}
.card .photo{width:130px;height:86px}
.card h3{font-family:"Montserrat",sans-serif;font-weight:500;font-size:8px;color:var(--white);margin:13px 12px 6px}
.card p{font-size:6.3px;line-height:12px;color:#e6ecf6;margin:0 12px}

/* portfolio band */
.portfolio{left:0;top:725px;width:691px;height:190px;background:linear-gradient(90deg,#4a4744,#5c5853 50%,#48443f)}
.portfolio .section-title{color:var(--white);top:27px}
.portfolio .lead{left:0;width:691px;top:48px;text-align:center;color:#eee;font-size:6.4px}
.thumb{top:76px;width:130px;height:82px;border:2px solid var(--white);box-shadow:0 3px 6px rgba(0,0,0,.4)}
.arrow{top:114px;width:9px;height:9px;border-radius:50%;background:rgba(255,255,255,.55)}

/* testimonials */
.avatar{width:60px;height:60px;border-radius:50%;border:2px solid #e6e6e6;box-shadow:0 1px 3px rgba(0,0,0,.2)}
.quote{font-size:6.4px;line-height:12.5px;color:#555}
.quote .by{display:block;color:var(--orange);margin-top:6px;font-size:6.4px}
.q{font-family:Georgia,serif;font-size:11px;color:#444;line-height:0}

/* footer */
.footer{left:0;top:1074px;width:691px;height:86px;background:var(--footer);color:var(--footer-text);font-size:6.2px;line-height:11px}
.footer h4{font-family:"Montserrat",sans-serif;font-weight:500;font-size:9px;color:var(--white);position:absolute;top:18px}
.news input{width:113px;height:24px;border:none;background:var(--white);font-size:6px;padding-left:8px;color:#aaa;font-family:"Roboto",sans-serif}
.news button{width:65px;height:24px;border:none;background:var(--orange);color:var(--white);font-size:6px;font-family:"Roboto",sans-serif}
.social{display:flex;gap:4px}
.social span{width:16px;height:16px;border-radius:50%;border:1.5px solid var(--white)}
.basebar{left:0;top:1160px;width:691px;height:40px;background:var(--footer-base);font-size:6px;color:#ddd}
.basebar .links{left:64px;top:16px}
.basebar .copy{right:65px;top:16px;color:#4d4d4d}
</style>
</head>
<body>

<div class="abs topbar">
  <span class="abs phone">PHONE : (555) 318-4470</span>
  <svg class="abs" width="8" height="8" viewBox="0 0 10 10"><circle cx="4" cy="4" r="3" fill="none" stroke="#fff" stroke-width="1.6"/><line x1="6.2" y1="6.2" x2="9" y2="9" stroke="#fff" stroke-width="1.8"/></svg>
</div>

<header class="abs header">
  <div class="abs brand"><span class="mark"></span><span class="name">BENVOE CABINETS</span></div>
  <nav class="abs nav">
    <a href="#">HOME</a><a href="#">ABOUT US</a><a href="#">PORTFOLIO</a><a href="#">ERVICES</a><a href="#">CONTACT US</a>
  </nav>
</header>

<section class="abs hero" role="img" aria-label="Bright white modern kitchen with pendant lights and a stone island">
  <div class="abs hero-caption">
    <h1>DIFFERENT AREAS OF THE HOME WE CAN PRODUCE CABINETS</h1>
    <p>Duis autem vel eum iriure dolor in hendrerit in vulputate velit esse molestie consequat, vel illum dolore eu feugiat nulla facilisis at vero eros et accumsan et iusto odio dignissim qui blandit praesent.</p>
  </div>
  <div class="abs dots"><span class="dot"></span><span class="dot on"></span><span class="dot"></span></div>
</section>

<h2 class="abs section-title" style="top:439px">WELCOME TO BENVOE CUSTOM CABINETS</h2>
<p class="abs intro-text">Nam liber tempor cum soluta nobis eleifend option congue nihil imperdiet doming id quod mazim placerat facer possim assum. Typi non habent claritatem insitam; est usus legentis in iis qui facit eorum claritatem. Investigationes demonstraverunt lectores legere me lius quod ii legunt saepius.</p>

<h2 class="abs section-title" style="top:501px">WE TURN YOUR DREAM INTO REALITY</h2>
<p class="abs sub">New construction or renovations, we turn your dream into reality.</p>

<article class="abs card" style="left:64px">
  <div class="photo" role="img" aria-label="Dark wood custom kitchen" style="background:linear-gradient(135deg,#6b4a2e,#a88a63 60%,#4a3424)"></div>
  <h3>CUSTOM HOMES</h3>
  <p>Lorem ipsum dolor sit amet, consectetuer adipiscing elit, sed diam nonummy nibh</p>
</article>
<article class="abs card" style="left:208px">
  <div class="photo" role="img" aria-label="Renovated kitchen with stainless appliances" style="background:linear-gradient(135deg,#5a4535,#b7aea2 55%,#3f3128)"></div>
  <h3>RENOVATION AND REPAIR</h3>
  <p>Ut wisi enim ad minim veniam, quis nostrud exerci tation ullamcorper suscipit lobortis</p>
</article>
<article class="abs card active" style="left:352px">
  <div class="photo" role="img" aria-label="Wood kitchen island with stone top" style="background:linear-gradient(135deg,#8b5632,#c9c2b8 55%,#7a4a2a)"></div>
  <h3>FURNITURE</h3>
  <p>Duis autem vel eum iriure dolor in hendrerit in vulputate velit esse molestie consequat</p>
</article>
<article class="abs card" style="left:497px">
  <div class="photo" role="img" aria-label="White kitchen with dark counters" style="background:linear-gradient(135deg,#3a3633,#d8d6d2 55%,#5b5651)"></div>
  <h3>WALK-IN CLOSETS</h3>
  <p>Claritas est etiam processus dynamicus, qui sequitur mutationem consuetudium</p>
</article>

<section class="abs portfolio" role="img" aria-label="Dimmed kitchen interior background">
  <h2 class="abs section-title">OUR PORTFOLIO</h2>
  <p class="abs lead">Lorem ipsum dolor sit amet, consectetuer adipiscing elit, sed diam nonummy nibh euismod tincidunt ut laoreet dolore magna aliquam erat volutpat.</p>
  <span class="abs arrow" style="left:42px"></span>
  <div class="abs thumb" style="left:64px;background:linear-gradient(135deg,#e8e8e6,#9a9894 60%,#4a4846)" role="img" aria-label="White kitchen with island stools"></div>
  <div class="abs thumb" style="left:208px;background:linear-gradient(135deg,#c9bfb2,#7d6f62 60%,#3e352e)" role="img" aria-label="Kitchen with range hood and island"></div>
  <div class="abs thumb" style="left:352px;background:linear-gradient(135deg,#d8d2b8,#6e5a40 60%,#2f271e)" role="img" aria-label="Open kitchen with pendant lights"></div>
  <div class="abs thumb" style="left:497px;background:linear-gradient(135deg,#efe8dc,#b7a88e 55%,#3a2e24)" role="img" aria-label="Cream cabinets with dark counters"></div>
  <span class="abs arrow" style="left:640px"></span>
</section>

<h2 class="abs section-title" style="top:940px">SATISFIED CUSTOMERS</h2>

<div class="abs avatar" style="left:64px;top:968px;background:linear-gradient(135deg,#c8b8a4,#7a6654)" role="img" aria-label="Customer portrait"></div>
<p class="abs quote" style="left:130px;top:978px;width:195px"><span class="q">“</span> Our complete kitchen and bathroom renovation designed and orchestrated by you has greatly improved the value of our house. <span class="q">”</span><span class="by">~ M. HALVORSEN</span></p>

<div class="abs avatar" style="left:353px;top:968px;background:linear-gradient(135deg,#e6e2da,#8a9aa0)" role="img" aria-label="Customer couple portrait"></div>
<p class="abs quote" style="left:421px;top:972px;width:205px"><span class="q">“</span> Thank you for your excellent work and assistance to meet the building code requirements and of course we are very pleased with the workmanship <span class="q">”</span><span class="by">~ T. OKAFOR</span></p>

<div class="abs dots" style="left:335px;top:1044px"><span class="dot" style="background:#ccc"></span><span class="dot" style="background:#444"></span><span class="dot"></span></div>

<footer class="abs footer">
  <h4 style="left:65px">CONTACT US</h4>
  <svg class="abs" style="left:68px;top:38px" width="6" height="8" viewBox="0 0 6 8"><path d="M3 0a3 3 0 0 1 3 3c0 2-3 5-3 5S0 5 0 3a3 3 0 0 1 3-3z" fill="var(--blue)"/><circle cx="3" cy="3" r="1" fill="#121212"/></svg>
  <p class="abs" style="left:78px;top:37px">BENVOE CUSTOM CABINETS LTD.<br>2710 Maplewood Avenue<br>Riverton, B.C. V0X 2K4</p>
  <svg class="abs" style="left:191px;top:39px" width="9" height="7" viewBox="0 0 9 7"><rect width="9" height="7" rx="1" fill="var(--blue)"/><path d="M0 1l4.5 3L9 1" stroke="#121212" fill="none"/></svg>
  <p class="abs" style="left:205px;top:37px">hello@benvoecabinets.example</p>
  <svg class="abs" style="left:191px;top:53px" width="8" height="8" viewBox="0 0 8 8"><rect width="8" height="8" rx="1" fill="var(--blue)"/><path d="M2 1.5c0 3 1.5 4.5 4.5 4.5" stroke="#121212" stroke-width="1.2" fill="none"/></svg>
  <p class="abs" style="left:205px;top:51px">(555) 318-4470</p>

  <h4 style="left:335px">NEWSLETTER SIGNUP</h4>
  <form class="abs news" style="left:335px;top:38px;display:flex"><input value="Email Address" aria-label="Email Address"><button type="button">SUBSCRIBE</button></form>

  <h4 style="left:530px">CONNECT US</h4>
  <div class="abs social" style="left:530px;top:38px">
    <span style="background:var(--blue)"></span><span style="background:#2b8fd6"></span><span style="background:#1f6fb0"></span><span style="background:#d34836"></span><span style="background:var(--orange)"></span>
  </div>
</footer>

<div class="abs basebar">
  <span class="abs links">CONTACT U &nbsp;&nbsp;|&nbsp;&nbsp; PRIVACY POLICY</span>
  <span class="abs copy">Copyright @ 2015 Benvoe Custom Cabinets. All Right Reserved.</span>
</div>

</body>
</html>
```